Sign Design

We already have a logo, but would like to design 2 x signs.
Sign 1:
Dimensions 1500mm wide x 2500m high.
Information to include on sign: - Clinic name and logo (attached)
- the word "DENTIST "
- Street number (which is 348)
Phone number (which is 6153 4097)

Sign 2:
Dimensions: 800mm wide x 600mm high

```html
<!DOCTYPE html>
<html lang="en">
<head>
<meta charset="utf-8">
<title>Kelbrook Dental Care – Sign Designs</title>
<link href="https://fonts.googleapis.com/css2?family=Arimo:wght@400;700&display=swap" rel="stylesheet">
<style>
  :root {
    --backdrop-center: #4a4849;
    --backdrop-edge: #272526;
    --green-deep: #137a36;
    --green-bright: #1fb52a;
    --green-lime: #9bd94b;
    --green-soft: #c9ec98;
    --green-pale: #e4f5c6;
    --white: #ffffff;
    --ink: #111111;
  }
  html, body {
    margin: 0;
    padding: 0;
    width: 1200px;
    height: 960px;
    overflow: hidden;
  }
  body {
    background: radial-gradient(ellipse at 50% 40%, var(--backdrop-center) 0%, var(--backdrop-edge) 75%);
    font-family: "Arimo", Arial, sans-serif;
    position: relative;
  }
  .sign {
    position: absolute;
    display: block;
    box-shadow: 0 2px 6px rgba(0,0,0,0.35);
  }
  .sign--fascia { left: 23px; top: 174px; width: 1154px; height: 193px; }
  .sign--panel  { left: 292px; top: 436px; width: 616px; height: 461px; }
  .clinic-name { fill: var(--green-deep); font-weight: 400; letter-spacing: -1.5px; }
  .clinic-tagline { fill: var(--green-bright); font-weight: 400; letter-spacing: -0.5px; }
  .word-dentist { fill: var(--green-lime); font-weight: 400; }
  .bar-label { fill: var(--ink); font-size: 22px; }
  .bar-label--light { fill: var(--green-pale); }
  .bar-value { font-weight: 700; font-size: 29px; }
</style>
</head>
<body>

  <!-- Sign 1: wide fascia sign -->
  <svg class="sign sign--fascia" viewBox="0 0 1154 193" xmlns="http://www.w3.org/2000/svg">
    <defs>
      <linearGradient id="fasciaFill" x1="0" x2="1" y1="0" y2="0">
        <stop offset="0" stop-color="#ffffff"/>
        <stop offset="0.35" stop-color="#f4fbe8"/>
        <stop offset="1" stop-color="#e2f4c2"/>
      </linearGradient>
      <linearGradient id="fasciaPhoto" x1="0" x2="0" y1="0" y2="1">
        <stop offset="0" stop-color="#5e4433"/>
        <stop offset="0.22" stop-color="#9c7458"/>
        <stop offset="0.45" stop-color="#dcab86"/>
        <stop offset="0.78" stop-color="#e9c3a3"/>
        <stop offset="1" stop-color="#f5f0ec"/>
      </linearGradient>
    </defs>
    <rect width="1154" height="193" fill="var(--white)"/>
    <polygon points="0,0 861,0 789,193 0,193" fill="url(#fasciaFill)"/>
    <polygon points="861,0 873,0 803,193 789,193" fill="var(--green-bright)"/>
    <polygon points="884,0 890,0 820,193 814,193" fill="var(--green-lime)"/>
    <rect x="880" y="0" width="274" height="193" fill="url(#fasciaPhoto)" role="img" aria-label="Photo of a smiling young couple"/>

    <circle cx="112" cy="88" r="62" fill="var(--green-lime)"/>
    <text class="clinic-name" x="205" y="90" font-size="62">Kelbrook</text>
    <text class="clinic-tagline" x="497" y="128" font-size="35" text-anchor="end">Dental Care</text>

    <text class="word-dentist" x="566" y="104" font-size="52">DENTIST</text>

    <polygon points="182,150 441,150 428,184 175,184" fill="var(--green-lime)"/>
    <polygon points="441,150 805,150 792,184 428,184" fill="var(--green-bright)"/>
    <text class="bar-label" x="198" y="176">Street number <tspan class="bar-value" x="360" fill="var(--ink)">348</tspan></text>
    <text class="bar-label bar-label--light" x="456" y="176">Phone number <tspan class="bar-value" x="622" fill="var(--green-pale)">6153 4097</tspan></text>
  </svg>

  <!-- Sign 2: panel sign -->
  <svg class="sign sign--panel" viewBox="0 0 616 461" xmlns="http://www.w3.org/2000/svg">
    <defs>
      <linearGradient id="panelFill" x1="0" x2="0" y1="0" y2="1">
        <stop offset="0" stop-color="#ffffff"/>
        <stop offset="1" stop-color="#e4f5c6"/>
      </linearGradient>
      <linearGradient id="panelPhoto" x1="0" x2="0" y1="0" y2="1">
        <stop offset="0" stop-color="#f4f1ee"/>
        <stop offset="0.08" stop-color="#6a4c38"/>
        <stop offset="0.26" stop-color="#a27b5e"/>
        <stop offset="0.42" stop-color="#dcab86"/>
        <stop offset="0.7" stop-color="#e8bf9d"/>
        <stop offset="0.88" stop-color="#f1dccb"/>
        <stop offset="1" stop-color="#f7f3f0"/>
      </linearGradient>
      <radialGradient id="panelPhotoGlow" cx="0.7" cy="0.5" r="0.5">
        <stop offset="0" stop-color="#f2cdae" stop-opacity="0.6"/>
        <stop offset="1" stop-color="#f2cdae" stop-opacity="0"/>
      </radialGradient>
    </defs>
    <rect width="616" height="461" fill="url(#panelFill)"/>
    <circle cx="210" cy="160" r="120" fill="var(--green-soft)" opacity="0.55"/>
    <polygon points="310,0 616,0 616,461 158,461" fill="url(#panelPhoto)" role="img" aria-label="Photo of a smiling young couple"/>
    <polygon points="310,0 616,0 616,461 158,461" fill="url(#panelPhotoGlow)"/>
    <polygon points="300,0 310,0 158,461 148,461" fill="var(--green-bright)"/>

    <rect x="0" y="332" width="616" height="110" fill="var(--white)" opacity="0.78"/>
    <rect x="0" y="442" width="616" height="19" fill="var(--green-pale)"/>

    <circle cx="175" cy="385" r="46" fill="var(--green-lime)"/>
    <text class="clinic-name" x="248" y="382" font-size="52">Kelbrook</text>
    <text class="clinic-tagline" x="476" y="416" font-size="30" text-anchor="end">Dental Care</text>
  </svg>

</body>
</html>
```